New business card for civil engineering company - "Keystone Audit"

We need a business card designed for our new structural engineering company.

The company name is "Keystone Audit" logo files attached.

We would like the following:
* Two-sided card
* Simple design

Information to be placed on the card:
Name - Marcus Dellow
Job Title - Director / Structural Engineer
Credentials - BEng(Hons), CPEng, CMengNZ, IntPE(NZ)
Email - marcus.dellow@keystoneaudit.co.nz
mobile - 0219364058
website - www.keystoneaudit.co.nz

```html
<!DOCTYPE html>
<html lang="en">
<head>
<meta charset="utf-8">
<title>Keystone Audit — Business Card</title>
<link rel="stylesheet" href="https://fonts.googleapis.com/css2?family=Exo+2:ital,wght@0,500;0,600;1,400&family=Open+Sans:wght@400&display=swap">
<style>
  :root {
    --backdrop: #c4c4c4;
    --navy: #1e3658;
    --navy-deep: #1b3a6e;
    --wave-light: #5e9bd6;
    --wave-mid: #3d6fae;
    --mark: #6a9fd4;
    --paper: #f4f4f4;
    --paper-shade: #e6e6e6;
    --ink: #2b2b2b;
    --ink-soft: #555a60;
    --front-ink: #e4eaf2;
    --front-soft: #b9c6d8;
  }
  * { margin: 0; padding: 0; box-sizing: border-box; }
  html, body {
    width: 1200px; height: 576px; overflow: hidden;
    background: var(--backdrop);
  }
  .canvas { position: relative; width: 1200px; height: 576px; }

  .card {
    position: absolute;
    top: 138px;
    height: 294px;
    box-shadow: 2px 3px 6px rgba(0,0,0,0.28);
    overflow: hidden;
  }

  .logo-mark {
    position: absolute;
    width: 60px; height: 60px;
    background: var(--mark);
  }

  /* Front */
  .card-front {
    left: 81px; width: 486px;
    background: var(--navy);
  }
  .card-front .logo-mark { left: 213px; top: 110px; }
  .front-lockup {
    position: absolute; left: 0; right: 0; top: 194px;
    text-align: center;
  }
  .company-name {
    font-family: "Exo 2", sans-serif;
    font-weight: 600;
    letter-spacing: 1.5px;
    text-transform: uppercase;
    white-space: nowrap;
  }
  .card-front .company-name { color: var(--front-ink); font-size: 21px; line-height: 1; }
  .tagline {
    font-family: "Exo 2", sans-serif;
    font-weight: 500;
    text-transform: uppercase;
    letter-spacing: 2.2px;
    font-size: 8.5px;
    margin-top: 6px;
    white-space: nowrap;
  }
  .card-front .tagline { color: var(--front-soft); }

  /* Back */
  .card-back {
    left: 602px; width: 480px; height: 292px;
    background: linear-gradient(160deg, var(--paper) 0%, #fafafa 45%, var(--paper-shade) 100%);
  }
  .wave { position: absolute; left: 0; top: 0; width: 480px; height: 292px; }

  .card-back .logo-mark { left: 62px; top: 148px; }

  .person {
    position: absolute; right: 22px; top: 22px;
    text-align: right; color: #fff;
  }
  .person-name {
    font-family: "Exo 2", sans-serif; font-weight: 600;
    font-size: 20px; line-height: 1.1;
  }
  .person-title {
    font-family: "Exo 2", sans-serif; font-style: italic; font-weight: 400;
    font-size: 11.5px; margin-top: 4px;
  }
  .person-credentials {
    font-family: "Open Sans", sans-serif; font-size: 10.5px;
    line-height: 18px; margin-top: 2px;
  }

  .back-lockup { position: absolute; left: 30px; top: 229px; }
  .card-back .company-name { color: var(--ink); font-size: 18px; letter-spacing: 1px; line-height: 1; }
  .card-back .tagline { color: var(--ink-soft); font-size: 7.4px; letter-spacing: 1.9px; margin-top: 7px; }

  .contact-list {
    position: absolute; right: 22px; top: 200px;
    list-style: none;
    font-family: "Open Sans", sans-serif; font-size: 11.5px;
    color: var(--ink);
  }
  .contact-item {
    display: flex; justify-content: flex-end; align-items: center;
    height: 18px;
    white-space: nowrap;
  }
  .contact-icon { width: 10px; height: 10px; margin-left: 10px; fill: #3a3a3a; flex: none; }
</style>
</head>
<body>
<main class="canvas">

  <section class="card card-front" aria-label="Card front">
    <div class="logo-mark" role="img" aria-label="Keystone Audit logo placeholder"></div>
    <div class="front-lockup">
      <div class="company-name">Keystone Audit</div>
      <div class="tagline">Peer Review Specialists</div>
    </div>
  </section>

  <section class="card card-back" aria-label="Card back">
    <svg class="wave" viewBox="0 0 480 292" aria-hidden="true">
      <defs>
        <linearGradient id="waveFill" x1="0" y1="0" x2="1" y2="0">
          <stop offset="0" stop-color="var(--wave-light)"/>
          <stop offset="0.55" stop-color="var(--wave-mid)"/>
          <stop offset="1" stop-color="var(--navy-deep)"/>
        </linearGradient>
      </defs>
      <path d="M0,0 H480 V146 C420,150 370,140 320,112 C240,66 160,48 40,60 C25,62 10,64 0,66 Z" fill="url(#waveFill)"/>
      <path d="M0,44 C110,18 220,34 300,84 C360,120 420,132 480,118" fill="none" stroke="#fff" stroke-width="7"/>
      <path d="M40,62 C140,40 230,58 300,102 C360,138 420,150 480,142" fill="none" stroke="#fff" stroke-width="6"/>
      <path d="M150,52 C220,56 270,80 315,110 C370,146 425,156 480,148" fill="none" stroke="var(--navy-deep)" stroke-width="5" opacity="0.8"/>
    </svg>

    <div class="person">
      <div class="person-name">Marcus Dellow</div>
      <div class="person-title">Director / Structural Engineer</div>
      <div class="person-credentials">BEng(Hons), CPEng,<br>CMengNZ, IntPE(NZ)</div>
    </div>

    <div class="logo-mark" role="img" aria-label="Keystone Audit logo placeholder"></div>
    <div class="back-lockup">
      <div class="company-name">Keystone Audit</div>
      <div class="tagline">Peer Review Specialists</div>
    </div>

    <ul class="contact-list">
      <li class="contact-item">0219364058
        <svg class="contact-icon" viewBox="0 0 12 12" aria-hidden="true"><path d="M1,4 C1,2 3,1 6,1 C9,1 11,2 11,4 L8.5,4.5 L8,3 C7,2.6 5,2.6 4,3 L3.5,4.5 Z M3,6 H9 L10,11 H2 Z"/></svg>
      </li>
      <li class="contact-item">www.keystoneaudit.co.nz
        <svg class="contact-icon" viewBox="0 0 12 12" aria-hidden="true"><path d="M1,2.5 H11 V9.5 H1 Z"/><path d="M1.5,3 L6,6.5 L10.5,3" fill="none" stroke="#fff" stroke-width="1"/></svg>
      </li>
      <li class="contact-item">marcus.dellow@keystoneaudit.co.nz
        <svg class="contact-icon" viewBox="0 0 12 12" aria-hidden="true"><circle cx="6" cy="6" r="5"/><path d="M1,6 H11 M6,1 C3.5,3.5 3.5,8.5 6,11 M6,1 C8.5,3.5 8.5,8.5 6,11" fill="none" stroke="#fff" stroke-width="0.8"/></svg>
      </li>
    </ul>
  </section>

</main>
</body>
</html>
```